Pest Control Company needs business card!

Hi there, we need a business card designed for our new Pest Control Company. Ideally this card will be simple, yet feel elegant and high end. We want to use the colours Orange, Black and White. Please see our attached logo for the exact colours.

Business card details:

Phone - 0461 275 804
Name - Gavin Holloway
Email - Info@steadfastverminguard.com.au

We would also like to include the following list with dot points:

SERVICES / INSPECTIONS

Termites, Wood Borers, Ants, Cockroaches, Spiders, Fleas, Mice, Rats, Bed Bugs, & More!

```html
<!DOCTYPE html>
<html lang="en">
<head>
<meta charset="utf-8">
<title>Steadfast Vermin Guard – Business Card</title>
<link href="https://fonts.googleapis.com/css2?family=Montserrat:wght@600;800&family=Arimo:wght@400&display=swap" rel="stylesheet">
<style>
  :root {
    --stage: #121212;
    --card: #2a2a2c;
    --card-shade: #242426;
    --orange: #f58220;
    --white: #f2f2f2;
    --rule: #4a4a4d;
  }
  * { box-sizing: border-box; margin: 0; padding: 0; }
  html, body {
    width: 1200px; height: 820px; overflow: hidden;
    background: var(--stage);
  }
  .stage {
    width: 1200px; height: 820px;
    display: flex; align-items: center; justify-content: center; gap: 44px;
  }
  .card {
    position: relative;
    width: 540px; height: 309px;
    background: linear-gradient(160deg, var(--card), var(--card-shade));
    border-bottom: 3px solid var(--orange);
    border-left: 2px solid var(--orange);
    box-shadow: 0 18px 40px rgba(0,0,0,.6);
    overflow: hidden;
    font-family: "Arimo", Arial, sans-serif;
    color: var(--white);
  }

  /* Front */
  .brand {
    position: absolute; top: 62px; right: 62px;
    display: flex; align-items: center; gap: 12px;
  }
  .brand-dot {
    width: 34px; height: 34px; border-radius: 50%;
    background: var(--orange);
  }
  .brand-name {
    font-family: "Montserrat", Arial, sans-serif;
    font-weight: 800; font-size: 26px; line-height: 1.05;
    color: var(--orange); text-transform: uppercase; letter-spacing: .5px;
  }
  .divider {
    position: absolute; left: 0; right: 0; top: 168px;
    height: 1px; background: var(--rule);
  }
  .holder {
    position: absolute; left: 40px; top: 186px;
    font-family: "Montserrat", Arial, sans-serif;
    font-weight: 800; font-size: 21px; letter-spacing: .5px;
    color: var(--orange); text-transform: uppercase;
  }
  .contacts {
    position: absolute; left: 40px; top: 222px;
    list-style: none; font-size: 14px; line-height: 22px;
  }
  .contacts li { display: flex; align-items: center; gap: 10px; }
  .contacts svg { width: 14px; height: 14px; fill: none; stroke: var(--orange); stroke-width: 2; }

  /* Back */
  .services {
    position: absolute; left: 40px; bottom: 48px;
  }
  .services-title {
    font-size: 13px; letter-spacing: .6px; text-transform: uppercase;
    margin-bottom: 18px;
  }
  .service-row { font-size: 15px; line-height: 22px; }
  .service-row span::before {
    content: ""; display: inline-block;
    width: 8px; height: 8px; border-radius: 50%;
    background: var(--orange); margin: 0 6px 1px 0;
  }
  .service-row span + span { margin-left: 6px; }
</style>
</head>
<body>
<main class="stage">

  <section class="card card-front">
    <div class="brand">
      <span class="brand-dot"></span>
      <span class="brand-name">Steadfast<br>Vermin Guard</span>
    </div>
    <div class="divider"></div>
    <h1 class="holder">Gavin Holloway</h1>
    <ul class="contacts">
      <li>
        <svg viewBox="0 0 24 24"><path d="M5 3h4l2 5-3 2a11 11 0 0 0 6 6l2-3 5 2v4a2 2 0 0 1-2 2A18 18 0 0 1 3 5a2 2 0 0 1 2-2z"/></svg>
        0461 275 804
      </li>
      <li>
        <svg viewBox="0 0 24 24"><rect x="2" y="5" width="20" height="14"/><path d="M2 5l10 8 10-8"/></svg>
        Info@steadfastverminguard.com.au
      </li>
      <li>
        <svg viewBox="0 0 24 24"><circle cx="12" cy="12" r="10"/><path d="M2 12h20M12 2c3 3 3 17 0 20M12 2c-3 3-3 17 0 20"/></svg>
        www.steadfastverminguard.com.au
      </li>
    </ul>
  </section>

  <section class="card card-back">
    <div class="services">
      <h2 class="services-title">Services / Inspections</h2>
      <p class="service-row"><span>Termites</span></p>
      <p class="service-row"><span>Wood Borers</span></p>
      <p class="service-row"><span>Ants</span><span>Cockroaches</span><span>Mice</span></p>
      <p class="service-row"><span>Spiders</span><span>Fleas</span></p>
      <p class="service-row"><span>Rats</span><span>Bed Bugs &amp; More!</span></p>
    </div>
  </section>

</main>
</body>
</html>
```